Pitch book for Birchvale Real Estate Investors.

Birchvale Investors is a new real estate investment company focused on multifamily (apartment) investments along the San Francisco Peninsula (in other parts of the world it is also referred to as flats). We need a professional Pitch Book i.e. brochure (digital and print) to raise equity from private investors. Read about “pitch book” on Wikipedia. The profile of the investor is conservative and must qualify as an accredited investor. Think high net worth individuals, CEOs and wealthy retiring couples. The investor that is attracted to real estate invest because it is low risk, produce cash flow and provide solid returns over the long term.

The brochure should convey trust, be highly professional and be clean and crisp. I attach a PowerPoint doc to be used as a copy for the brochure. I also attach a brochure of Harlow Pike – I like the look and feel, think it was designed with InDesign.

We will use the brochure at one-on-one meetings with investors where we will present on a laptop; we also need it in a format so that we can email it, print it and use it to be uploaded as a website.

I prefer the up and down scroll format (like you would do on a Mac) compared to PowerPoint but I am open to suggestions.

The photos I used in the PowerPoint presentation was found on the web, please use your own stock images.

Target Market(s)

High net worth individuals

Industry/Entity Type

Real Estate

Font styles to use
Serif

Requirements
Must have
• See attached Power Point
Nice to have
• See attached HPK brochure, I like the look and feel.
Should not have
• I am open to your ideas.

```html
<!DOCTYPE html>
<html lang="en">
<head>
<meta charset="utf-8">
<title>Birchvale Real Estate Investors – Growth in Sales Prices</title>
<link href="https://fonts.googleapis.com/css2?family=EB+Garamond:wght@400;500&display=swap" rel="stylesheet">
<style>
  :root {
    --backdrop: #a4a4a4;
    --paper: #fbfbfa;
    --gold: #b8902f;
    --gold-line: #d2ae5a;
    --blue: #2f7fc8;
    --blue-line: #6ea3d6;
    --teal: #15917a;
    --teal-line: #4fae9a;
    --ink: #3a3a3a;
    --sky: #8fb7d6;
    --land: #7b8a78;
  }
  * { box-sizing: border-box; margin: 0; padding: 0; }
  html, body { width: 1200px; height: 800px; overflow: hidden; }
  body {
    background: var(--backdrop);
    font-family: "EB Garamond", Georgia, serif;
    color: var(--ink);
  }
  .spread {
    position: absolute;
    left: 60px; top: 120px;
    width: 1080px; height: 560px;
    display: flex;
    box-shadow: 0 12px 30px rgba(0,0,0,.25);
  }
  .page { width: 540px; height: 560px; position: relative; background: var(--paper); }

  /* left page */
  .hero-photo {
    position: absolute; inset: 0;
    background: linear-gradient(172deg, var(--sky) 0%, #a9c3d4 18%, #6d8a99 34%, var(--land) 55%, #8b9288 75%, #6f7d6a 100%);
  }
  .title-band {
    position: absolute; left: 0; top: 120px;
    width: 360px; padding: 18px 0 18px 56px;
    background: var(--gold);
    color: #fff;
  }
  .title-band h1 {
    font-weight: 400; font-size: 30px; letter-spacing: .04em; line-height: 1;
  }
  .title-band p {
    font-size: 15px; letter-spacing: .12em; margin-top: 6px;
  }

  /* right page */
  .page--right { background: linear-gradient(90deg, #e8e8e6 0%, var(--paper) 4%); }
  .sales-table {
    position: absolute; left: 30px; top: 52px;
    border-collapse: separate; border-spacing: 7px 3px;
    font-size: 10.5px;
  }
  .group-label th {
    font-weight: 400; font-size: 11px; letter-spacing: .05em; padding-bottom: 2px;
  }
  .col-head th {
    color: #fff; font-weight: 400; font-size: 11px; letter-spacing: .06em;
    padding: 4px 6px; border-radius: 2px 2px 0 0;
  }
  .head--address { background: var(--blue); }
  .head--units, .head--date { background: var(--gold); }
  .head--price { background: var(--teal); }
  td { height: 21px; text-align: center; padding: 0 6px; white-space: nowrap; }
  .cell--address { border: 1px solid var(--blue-line); width: 200px; text-align: left; }
  .cell--units, .cell--date { border: 1px solid var(--gold-line); width: 50px; }
  .cell--price { border: 1px solid var(--teal-line); width: 76px; }
  .page-marker {
    position: absolute; right: 14px; bottom: 10px;
    width: 8px; height: 14px; background: #8a8a8a;
  }
</style>
</head>
<body>
  <div class="spread">
    <section class="page page--left">
      <div class="hero-photo" role="img" aria-label="Aerial photograph of San Mateo County shoreline with lagoons, freeways and bay"></div>
      <div class="title-band">
        <h1>GROWTH IN SALES PRICES</h1>
        <p>SAN MATEO COUNTY</p>
      </div>
    </section>

    <section class="page page--right">
      <table class="sales-table">
        <thead>
          <tr class="group-label">
            <th></th>
            <th colspan="3">HISTORIC SALE</th>
            <th>2014 SALE</th>
          </tr>
          <tr class="col-head">
            <th class="head--address">PROPERTY ADDRESS</th>
            <th class="head--units">UNITS</th>
            <th class="head--date">DATE</th>
            <th class="head--price">PRICE</th>
            <th class="head--price">PRICE</th>
          </tr>
        </thead>
        <tbody>
          <tr><td class="cell--address">210 Alder Crest Road, Belmont</td><td class="cell--units">69</td><td class="cell--date">2006</td><td class="cell--price">13,500,000</td><td class="cell--price">23,750,000</td></tr>
          <tr><td class="cell--address">305-327 Linden Way, Belmont</td><td class="cell--units">65</td><td class="cell--date">2006</td><td class="cell--price">9,864,000</td><td class="cell--price">17,550,000</td></tr>
          <tr><td class="cell--address">740 Harborview Blvd, San Mateo</td><td class="cell--units">45</td><td class="cell--date">2012</td><td class="cell--price">10,950,000</td><td class="cell--price">16,450,000</td></tr>
          <tr><td class="cell--address">1315 Vista Ridge Avenue, San Mateo</td><td class="cell--units">70</td><td class="cell--date">2004</td><td class="cell--price">4,275,751</td><td class="cell--price">14,200,000</td></tr>
          <tr><td class="cell--address">1527 Willow Street, San Mateo</td><td class="cell--units">28</td><td class="cell--date">2012</td><td class="cell--price">6,300,000</td><td class="cell--price">9,490,000</td></tr>
          <tr><td class="cell--address">786 Ashford Street, Redwood City</td><td class="cell--units">25</td><td class="cell--date">2003</td><td class="cell--price">2,950,000</td><td class="cell--price">7,125,000</td></tr>
          <tr><td class="cell--address">409 E Maple Avenue, San Mateo</td><td class="cell--units">31</td><td class="cell--date">2012</td><td class="cell--price">4,340,000</td><td class="cell--price">6,550,000</td></tr>
          <tr><td class="cell--address">38 E 43rd Place, San Mateo</td><td class="cell--units">20</td><td class="cell--date">2008</td><td class="cell--price">3,666,500</td><td class="cell--price">5,600,000</td></tr>
          <tr><td class="cell--address">907 Cordova Street, Belmont</td><td class="cell--units">19</td><td class="cell--date">1990</td><td class="cell--price">1,550,000</td><td class="cell--price">4,650,000</td></tr>
          <tr><td class="cell--address">209 6th Avenue, Belmont</td><td class="cell--units">20</td><td class="cell--date">2006</td><td class="cell--price">2,150,000</td><td class="cell--price">4,300,000</td></tr>
          <tr><td class="cell--address">2457 Fairfield Road, Redwood City</td><td class="cell--units">18</td><td class="cell--date">2012</td><td class="cell--price">2,200,000</td><td class="cell--price">3,650,000</td></tr>
          <tr><td class="cell--address">647 Hollis Way, Belmont</td><td class="cell--units">10</td><td class="cell--date">1990</td><td class="cell--price">985,000</td><td class="cell--price">3,550,000</td></tr>
          <tr><td class="cell--address">456 Whitmore Avenue, Redwood City</td><td class="cell--units">11</td><td class="cell--date">2012</td><td class="cell--price">1,617,000</td><td class="cell--price">3,325,000</td></tr>
          <tr><td class="cell--address">966 F Street, Belmont</td><td class="cell--units">12</td><td class="cell--date">2004</td><td class="cell--price">1,980,000</td><td class="cell--price">2,900,000</td></tr>
          <tr><td class="cell--address">1126 Castillo Street, Redwood City</td><td class="cell--units">10</td><td class="cell--date">2005</td><td class="cell--price">1,475,000</td><td class="cell--price">2,325,000</td></tr>
          <tr><td class="cell--address">1158 Elmwood Avenue, San Carlos</td><td class="cell--units">17</td><td class="cell--date">2005</td><td class="cell--price">1,540,000</td><td class="cell--price">2,175,000</td></tr>
        </tbody>
      </table>
      <div class="page-marker"></div>
    </section>
  </div>
</body>
</html>
```